New Website Design & Build Project - Bright Fork Kitchen

I am looking for a professional clean looking website design then build of a website for my meal delivery business Bright Fork Kitchen. I already have the domain - www.brightforkkitchen.com.au and I will upload brief for the design and layout of the website.

I have a dropbox full of photos, designs, videos and existing graphic design work that I can share with the designers. This can be provided upon designer request.

I am looking to build this site in WORDPRESS and I would like to build the site using the Kestrel Page Composer - https://kestrellayouts.com/

Target Market(s)

Kids from 2-16 , Teenagers - 16 - 19, Adults - 19 - 80 + - We Cater For Everyone

Industry/Entity Type

Health And Wellness

Coding

Coded - Design and coding required

Number of Pages Required

5+ page

Colors
33b8a4
abd037
ec1f27
fbee3f
3276b5

Requirements
Must have
• Must incorporate the included Bright Fork Kitchen & BFK Logo
Must incorporate designs of packaging into website design.
Must keep text styles consistant throughout design
Must be mobile, tablet and desktop view responsive on all devices.
Must be built in Wordpress
The coder must have experience with kestrel layouts, kestrel page composer, kestrel captures and also be very experienced with setting up products using Zap Vendor plug in-
https://zapvendor.com/
I want to integrate Mailowl - https://dealnook.com/mailowl/ into site as well
Nice to have
• All of the above
Should not have
• No dark colours

```html
<!DOCTYPE html>
<html lang="en">
<head>
<meta charset="utf-8">
<title>Bright Fork Kitchen</title>
<link href="https://fonts.googleapis.com/css2?family=Poppins:wght@300;400;500;600;700&display=swap" rel="stylesheet">
<style>
:root{
  --green:#6cc04a;
  --green-soft:#eef6e8;
  --ink:#111111;
  --text:#333333;
  --muted:#777777;
  --hero-bg:#f6f7f1;
  --line:#e3e3e3;
  --black:#000000;
  --white:#ffffff;
}
*{box-sizing:border-box;margin:0;padding:0}
html,body{width:1200px;height:3021px;overflow:hidden;background:var(--white)}
body{position:relative;font-family:"Poppins",sans-serif;color:var(--text)}
.abs{position:absolute}
.brand{font-weight:700;color:var(--ink);font-size:22px;letter-spacing:.5px;display:flex;align-items:center;gap:10px}
.brand .dot{width:16px;height:16px;background:var(--green);border-radius:50%}
.nav{top:40px;left:490px;display:flex;gap:23px;font-size:14px;color:var(--ink);align-items:center}
.nav .active{color:var(--green);border-bottom:1px solid var(--green);padding-bottom:3px}
.signup-tab{left:1002px;top:0;width:198px;height:94px;background:var(--green);color:var(--white);font-size:21px;font-weight:500;display:flex;align-items:center;justify-content:center;gap:18px}
.hero{left:0;top:0;width:1200px;height:680px;background:var(--hero-bg)}
h1,h2{color:var(--ink);font-weight:600;line-height:1.1}
.hero-title{left:77px;top:250px;font-size:52px;font-weight:700;line-height:1}
.hero-sub{left:79px;top:370px;font-size:19px;color:var(--green)}
.hero-text{left:79px;top:410px;font-size:16px;line-height:25px;width:300px}
.btn{background:var(--green);color:var(--white);font-size:19px;font-weight:500;display:flex;align-items:center;justify-content:center;gap:16px;border-radius:3px}
.dots{left:79px;top:641px;display:flex;gap:8px}
.dots span{width:8px;height:8px;border-radius:50%;background:#aaa}
.dots span:first-child{background:var(--green)}
.photo{border-radius:0}
.section-title{font-size:38px;font-weight:600}
.menu-cats{right:82px;top:1247px;text-align:right;font-size:16px;color:var(--ink);line-height:37.5px}
.card-title{font-size:18px;font-weight:500;line-height:23px}
.price{font-size:27px;color:var(--green)}
.blog-card{left:319px;width:562px;height:188px;border:1px solid var(--line);background:var(--white)}
.blog-date{position:absolute;left:34px;top:34px;font-size:14px;color:var(--ink)}
.blog-head{position:absolute;left:34px;top:64px;font-size:19px;font-weight:600;color:var(--ink);line-height:28px}
.blog-more{position:absolute;left:36px;top:133px;font-size:14px;color:var(--green)}
.field{left:362px;width:426px;border-bottom:1px solid var(--line);font-size:15px;color:var(--text);padding:0 4px 12px}
.foot-h{font-size:16px;font-weight:500;color:var(--ink)}
.foot-list{list-style:none;font-size:15px;line-height:27px}
.foot-list li::before{content:"";display:inline-block;width:6px;height:6px;border-radius:50%;background:var(--green);margin-right:11px;vertical-align:middle}
.social{width:40px;height:40px;border:1.5px solid var(--green);border-radius:50%;display:flex;align-items:center;justify-content:center}
</style>
</head>
<body>

<div class="abs hero"></div>
<div class="abs photo" role="img" aria-label="Noodle bowl with beef, greens, chopsticks and spring onion dish" style="left:490px;top:200px;width:640px;height:480px;background:radial-gradient(circle at 42% 55%,#6b4a2e 0,#3a3430 38%,#e9eee0 62%,var(--hero-bg) 75%)"></div>

<header>
  <div class="abs brand" style="left:77px;top:30px"><span class="dot"></span>BRIGHT FORK KITCHEN</div>
  <nav class="abs nav">
    <span class="active">HOME</span><span>MENU</span><span>SUPPLEMENYT</span><span>BLOG</span><span>CONTACT</span>
    <svg width="20" height="18" viewBox="0 0 20 18"><path d="M1 2h3l2 10h10l2-7H5" fill="none" stroke="#111" stroke-width="1.6"/><circle cx="8" cy="15.5" r="1.5" fill="#111"/><circle cx="15" cy="15.5" r="1.5" fill="#111"/></svg>
    <span style="margin-left:-12px">Sign Up</span>
  </nav>
  <div class="abs signup-tab">Sign Up
    <svg width="34" height="12" viewBox="0 0 34 12"><path d="M0 6h32M27 1l5 5-5 5" fill="none" stroke="#fff" stroke-width="1.5"/></svg></div>
</header>

<section>
  <h1 class="abs hero-title">BRIGHT FORK<br>KITCHEN</h1>
  <p class="abs hero-sub">Healthy Meals food in Harrowdale</p>
  <p class="abs hero-text">Weightloss – Strength &amp; Toning – Competition</p>
  <a class="abs btn" style="left:78px;top:472px;width:182px;height:54px">JOIN NOW
    <svg width="34" height="12" viewBox="0 0 34 12"><path d="M0 6h32M27 1l5 5-5 5" fill="none" stroke="#fff" stroke-width="1.5"/></svg></a>
  <div class="abs dots"><span></span><span></span><span></span><span></span></div>
</section>

<section>
  <h2 class="abs section-title" style="left:241px;top:756px">BRIGHT FORK KITCHEN<br>SUBSCRIPTION SERVICE</h2>
  <p class="abs" style="left:242px;top:862px;width:480px;font-size:16px;line-height:25px;color:var(--ink)">Join the Bright Fork Kitchen subscription service to get the lowest prices. Cancel anytime</p>
  <a class="abs btn" style="left:243px;top:928px;width:182px;height:54px">JOIN NOW
    <svg width="34" height="12" viewBox="0 0 34 12"><path d="M0 6h32M27 1l5 5-5 5" fill="none" stroke="#fff" stroke-width="1.5"/></svg></a>
</section>

<section>
  <h2 class="abs section-title" style="left:79px;top:1060px">OUR MENU</h2>
  <div class="abs" role="img" aria-label="Pita filled with grilled meat and herbs" style="left:0;top:1138px;width:274px;height:262px;background:linear-gradient(135deg,#6a4a2a,#d9c7a3 55%,#5d3b22)"></div>
  <div class="abs" style="left:0;top:1400px;width:274px;height:123px;background:var(--white);border-left:10px solid #3a3a3a">
    <p class="card-title" style="position:absolute;left:31px;top:26px;color:var(--ink)">BFK Kids 7 Day Meal<br>Plan</p>
    <p class="price" style="position:absolute;left:38px;top:80px">$35</p>
  </div>
  <div class="abs" role="img" aria-label="Plate of spiced rice with herbs, lime and yoghurt on dark stone" style="left:302px;top:1138px;width:541px;height:385px;background:linear-gradient(135deg,#3c3c3c,#7d7a70 35%,#d9a94a 55%,#4a4a48)"></div>
  <div class="abs" style="left:581px;top:1398px;width:262px;height:125px;background:var(--green);color:var(--white)">
    <p class="card-title" style="position:absolute;left:32px;top:28px">BFK Adult 7 Day Meal<br>Plan</p>
    <p class="price" style="position:absolute;left:38px;top:82px;color:var(--white)">$54</p>
  </div>
  <div class="abs menu-cats">Kids Meals<br>Vegetarian/Vegan<br>Beverages<br>Specials<br>Supplements</div>
  <div class="abs" style="left:1150px;top:1412px;width:50px;height:2px;background:var(--green)"></div>
  <svg class="abs" style="left:773px;top:1547px" width="68" height="14" viewBox="0 0 68 14"><path d="M28 7H2M7 2L2 7l5 5" fill="none" stroke="#444" stroke-width="1.5"/><path d="M40 7h26M61 2l5 5-5 5" fill="none" stroke="#111" stroke-width="1.5"/></svg>
</section>

<section>
  <div class="abs" role="img" aria-label="Athletic couple holding dumbbells" style="left:885px;top:1670px;width:315px;height:720px;background:linear-gradient(180deg,#ffffff,#e8c4a8 20%,#c9906e 50%,#5a5a5a 80%,#ffffff)"></div>
  <h2 class="abs section-title" style="left:0;width:1200px;text-align:center;top:1638px;font-size:40px">BRIGHT LIFE BLOG</h2>
  <article class="abs blog-card" style="top:1724px">
    <p class="blog-date">11 April, 2020</p>
    <p class="blog-head">Lorem Ipsum is simply<br>dummy text of the !</p>
    <p class="blog-more">LEARN MORE ▸</p>
    <div role="img" aria-label="Man holding a tray of healthy food" style="position:absolute;left:343px;top:-1px;width:219px;height:188px;background:linear-gradient(135deg,#7a4a2c,#3b4e6e 55%,#8a5a38)"></div>
  </article>
  <article class="abs blog-card" style="top:1935px">
    <p class="blog-date">11 April, 2020</p>
    <p class="blog-head">Lorem Ipsum is simply<br>dummy text of the !</p>
    <p class="blog-more">LEARN MORE ▸</p>
    <div role="img" aria-label="Bowl of avocado and mixed vegetable salad" style="position:absolute;left:343px;top:-1px;width:219px;height:188px;background:linear-gradient(135deg,#3a4a2a,#9cbc50 50%,#b8473a)"></div>
  </article>
  <p class="abs" style="left:520px;top:2157px;font-size:19px;font-weight:500;color:var(--green);display:flex;gap:14px;align-items:center">Explore More
    <svg width="28" height="12" viewBox="0 0 28 12"><path d="M0 6h26M21 1l5 5-5 5" fill="none" stroke="#6cc04a" stroke-width="1.5"/></svg></p>
</section>

<section>
  <div class="abs" style="left:0;top:2264px;width:304px;height:383px;background:var(--black)"></div>
  <h2 class="abs section-title" style="left:79px;top:2414px;color:var(--white)">MEMBER<br>SIGN UP</h2>
  <div class="abs" style="left:848px;top:2388px;width:352px;height:278px;background:var(--green)"></div>
  <p class="abs" style="left:364px;top:2296px;width:410px;font-size:16px;line-height:25px">Ready-made meals &amp; FREE* food delivery to your door with no lock-in contracts</p>
  <div class="abs field" style="top:2385px">Full Name</div>
  <div class="abs field" style="top:2458px">Mobile Number</div>
  <div class="abs field" style="top:2531px">Email</div>
  <a class="abs btn" style="left:361px;top:2582px;width:172px;height:54px">SIGN UP
    <svg width="34" height="12" viewBox="0 0 34 12"><path d="M0 6h32M27 1l5 5-5 5" fill="none" stroke="#fff" stroke-width="1.5"/></svg></a>
</section>

<footer>
  <div class="abs brand" style="left:77px;top:2773px;font-size:20px"><span class="dot"></span>BRIGHT FORK KITCHEN</div>
  <svg class="abs" style="left:77px;top:2838px" width="20" height="20" viewBox="0 0 20 20"><circle cx="10" cy="10" r="8.5" fill="none" stroke="#6cc04a" stroke-width="1.5"/><path d="M10 5v5h4" fill="none" stroke="#6cc04a" stroke-width="1.5"/></svg>
  <p class="abs" style="left:112px;top:2835px;font-size:15px;line-height:26px">Mon - Friday : 9-5 pm<br>Sat - 8 am &nbsp;&nbsp;&nbsp;: 12 pm</p>

  <p class="abs foot-h" style="left:337px;top:2733px">SITEMAP</p>
  <ul class="abs foot-list" style="left:337px;top:2765px"><li>Home</li><li>About</li><li>Menu</li><li>Supplement</li><li>Blog</li><li>Contact</li></ul>

  <p class="abs foot-h" style="left:541px;top:2733px">CONTACT US</p>
  <svg class="abs" style="left:541px;top:2764px" width="20" height="20" viewBox="0 0 20 20"><path d="M4 2l4 1 1 4-2 2a11 11 0 004 4l2-2 4 1 1 4-3 2C9 18 2 11 2 5z" fill="#6cc04a"/></svg>
  <p class="abs" style="left:578px;top:2764px;font-size:16px">0400 555 219</p>
  <svg class="abs" style="left:541px;top:2806px" width="22" height="16" viewBox="0 0 22 16"><rect x="1" y="1" width="20" height="14" fill="#6cc04a"/><path d="M1 1l10 8 10-8" fill="none" stroke="#fff" stroke-width="1.5"/></svg>
  <p class="abs" style="left:581px;top:2801px;font-size:15px;line-height:23px">mia@brightfork<br>health.com</p>
  <div class="abs" style="left:541px;top:2854px;display:flex;gap:6px">
    <div class="social"><svg width="14" height="14" viewBox="0 0 14 14"><circle cx="7" cy="7" r="3" fill="#6cc04a"/></svg></div>
    <div class="social"><svg width="14" height="14" viewBox="0 0 14 14"><circle cx="7" cy="7" r="3" fill="#6cc04a"/></svg></div>
    <div class="social"><svg width="14" height="14" viewBox="0 0 14 14"><circle cx="7" cy="7" r="3" fill="#6cc04a"/></svg></div>
  </div>

  <p class="abs foot-h" style="left:807px;top:2733px">SUBSCRIBE TO OUR NEWSLETTER</p>
  <p class="abs" style="left:807px;top:2760px;width:290px;font-size:15px;line-height:25px">Sign up for our newsletter to get the latest updates !</p>
  <div class="abs" style="left:806px;top:2813px;width:316px;height:56px;border:1px solid var(--line);border-radius:4px;box-shadow:0 2px 6px rgba(0,0,0,.06)">
    <span style="position:absolute;left:22px;top:17px;font-size:14px;color:var(--muted)">Enter Email *</span>
    <div style="position:absolute;right:4px;top:5px;width:46px;height:44px;background:var(--green);border-radius:3px;display:flex;align-items:center;justify-content:center">
      <svg width="18" height="18" viewBox="0 0 18 18"><path d="M1 9L17 1l-4 16-4-6z" fill="#fff"/></svg></div>
  </div>

  <div class="abs" style="left:77px;top:2948px;width:1046px;height:1px;background:var(--line)"></div>
  <p class="abs" style="left:0;width:1200px;text-align:center;top:2979px;font-size:15px">©BRIGHT FORK KITCHEN -2020 All rights reserved.</p>
</footer>

</body>
</html>
```